Book Cover Design for a Novella

This book is a whimsical book about random philosophical thoughts. The size of the book is 4X6 inches, about 140 pages long. I would like the background color to be maroon. The title of the book is The Copper Lanterns Beneath a Wandering Orchard, and the author name is Delia Thornquist. I would like the lettering to either be black or gold, in a font that looks like handwriting. From the lower left corner of the front cover, I would like there to be a gold-colored gardenia.
On the back cover, this is the book summary/description: “We are meant to share our hearts, not give them away. Vulnerability is not the act of placing your heart in someone else’s hands, saying, ‘Keep this safe for me.’ Vulnerability is wearing your heart on your sleeve, showing others your beauty, truths, and fears, and trusting that they will respect you.”
For the author's bio: Delia Thornquist is a native of Boulder, Colorado. She enjoys spending time with her cats, eating pasta, and contemplating random things, such as banana spiders, sewage systems, and other huge things that scare her.
I would like all the writing on the back to be in a black, regular font.
I will upload the author's photo, which I would like to be put next to the bio, and I will also attach a rough sketch of what I'd like the cover to look like. Message me with any questions! Thanks.

```html
<!DOCTYPE html>
<html lang="en">
<head>
<meta charset="utf-8">
<title>Back Cover</title>
<link rel="stylesheet" href="https://fonts.googleapis.com/css2?family=Allura&display=swap">
<style>
  :root {
    --maroon-bright: #8c0204;
    --maroon-mid: #6a0002;
    --maroon-deep: #2e0000;
    --ink: #0a0000;
    --glow: rgba(200, 10, 10, 0.75);
    --photo-light: #b9b7b0;
    --photo-dark: #5a4a3e;
  }
  html, body {
    margin: 0;
    padding: 0;
    overflow: hidden;
    background: var(--maroon-deep);
  }
  .back-cover {
    position: relative;
    width: 798px;
    height: 1200px;
    overflow: hidden;
    background:
      radial-gradient(ellipse 95% 80% at 15% 30%, var(--maroon-bright) 0%, var(--maroon-mid) 45%, transparent 100%),
      linear-gradient(135deg, var(--maroon-mid) 0%, var(--maroon-deep) 100%);
    font-family: "Allura", cursive;
    color: var(--ink);
    text-shadow: 0 0 6px var(--glow), 0 0 2px var(--glow);
  }
  .summary {
    position: absolute;
    left: 60px;
    top: 124px;
    width: 678px;
    margin: 0;
    text-align: center;
    font-size: 31px;
    line-height: 40px;
  }
  .bio-heading {
    position: absolute;
    right: 84px;
    top: 598px;
    margin: 0;
    font-size: 31px;
    font-weight: normal;
    line-height: 40px;
  }
  .bio-text {
    position: absolute;
    right: 84px;
    top: 674px;
    margin: 0;
    text-align: right;
    font-size: 31px;
    line-height: 37.5px;
  }
  .author-photo {
    position: absolute;
    left: 58px;
    top: 764px;
    width: 292px;
    height: 382px;
    background: linear-gradient(180deg, var(--photo-light) 0%, #9c8f80 45%, var(--photo-dark) 100%);
  }
</style>
</head>
<body>
  <main class="back-cover">
    <p class="summary">
      “We are meant to share our hearts, not give them away.<br>
      Vulnerability is not the act of placing your heart in<br>
      someone else’s hands, saying, ‘Keep this safe for me.’<br>
      Vulnerability is wearing your heart on your sleeve,<br>
      showing others your beauty, truths, and fears, and<br>
      trusting that they will respect you.”
    </p>

    <h2 class="bio-heading">Author’s Bio:</h2>
    <p class="bio-text">
      Delia Thornquist is a native of Boulder,<br>
      Colorado. She enjoys spending<br>
      time with her cats, eating<br>
      pasta, and contemplating<br>
      random things, such as<br>
      banana spiders, sewage<br>
      systems, and other huge<br>
      things that scare her.
    </p>

    <div class="author-photo" role="img" aria-label="Author portrait photograph of Delia Thornquist"></div>
  </main>
</body>
</html>
```